Summit Glossfloor & Honing
I'm looking for a business card and logo design for my
new Polished Concrete & Grinding business,
If you were to look up Summit in the dictionary it would
say, first in importance, order, or position; leading.
Polished Concrete floors are a niche market, that are being used currently in Shopping centres, office spaces and by most high end architects, builders and designers.
i need my business card & logo to stand out from my
competitors, i need my design + logo to reflect this it
needs to be simple, professional, eye catching, easy
to read and scream quality. The logo will need to be
suitable for a whole range of applications including,
uniforms, letter heads, stickers, and eventually
incorporating in vehicle vinyl wrapping.
Target Market(s)
Builders, architects, Interior designers & home owners
Contact Information for Business Card
Front side:
- Summit Glossfloor & Honing.
- Logo
Rear side:
- Liam Varga
- 0491735082
- info@summitgfh.com.au
- commercial - domestic - industrial
- (later down the line website & space for
social media links
www.summitglossfloor.com.au)
Colors
Designer to choose colors to be used in the design.
Look and feel

```html
<!DOCTYPE html>
<html lang="en">
<head>
<meta charset="utf-8">
<title>Summit Glossfloor &amp; Honing – Business Card</title>
<link rel="stylesheet" href="https://fonts.googleapis.com/css2?family=Oswald:wght@500;600&family=Roboto:wght@400;500&family=Roboto+Condensed:wght@400&display=swap">
<style>
  :root {
    --backdrop: #2b2b2b;
    --card-white: #ffffff;
    --card-fade: #e4e4e4;
    --card-black: #161616;
    --brand-blue: #1f9fd8;
    --brand-blue-deep: #1b8cc2;
    --ink: #1e1e1e;
    --ink-soft: #d7eef9;
    --paper-text: #f2f2f2;
  }
  * { margin: 0; padding: 0; box-sizing: border-box; }
  html, body { width: 1200px; height: 900px; overflow: hidden; }
  body {
    background: var(--backdrop);
    font-family: "Roboto", Arial, sans-serif;
    position: relative;
  }
  .card {
    position: absolute;
    left: 290px;
    width: 620px;
    height: 379px;
    border-radius: 20px;
    overflow: hidden;
    box-shadow: 0 10px 30px rgba(0,0,0,.45);
  }
  /* Front (name side) */
  .card-front {
    top: 40px;
    background: linear-gradient(160deg, var(--card-fade) 0%, var(--card-white) 45%, var(--card-white) 100%);
  }
  .name-band {
    position: absolute;
    left: 0; top: 42px;
    width: 500px; height: 100px;
    background: var(--brand-blue);
    border-radius: 0 50px 50px 0;
  }
  .person-name {
    position: absolute;
    left: 64px; top: 52px;
    font-family: "Oswald", "Arial Narrow", sans-serif;
    font-weight: 600;
    font-size: 42px;
    letter-spacing: 1px;
    text-transform: uppercase;
    color: var(--card-white);
  }
  .person-role {
    position: absolute;
    left: 48px; top: 104px;
    font-size: 15px;
    color: var(--ink-soft);
  }
  .brand-name {
    position: absolute;
    font-family: "Oswald", "Arial Narrow", sans-serif;
    font-weight: 600;
    text-transform: uppercase;
    color: var(--brand-blue-deep);
    line-height: 1.05;
  }
  .card-front .brand-name {
    right: 40px; top: 168px;
    font-size: 30px;
    text-align: right;
  }
  .contact-list {
    position: absolute;
    left: 34px; top: 236px;
    list-style: none;
    font-size: 17px;
    color: var(--ink);
  }
  .contact-list li { display: flex; align-items: center; gap: 10px; margin-bottom: 8px; }
  .contact-list svg { width: 14px; height: 14px; fill: var(--brand-blue); }
  .website {
    position: absolute;
    right: 40px; bottom: 30px;
    font-size: 17px;
    color: var(--ink);
  }
  /* Back (brand side) */
  .card-back {
    top: 481px;
    background: var(--card-black);
  }
  .card-back .brand-name {
    left: 0; right: 0; top: 100px;
    text-align: center;
    font-size: 46px;
    color: var(--brand-blue);
  }
  .sectors {
    position: absolute;
    left: 0; right: 0; bottom: 70px;
    text-align: center;
    font-family: "Roboto Condensed", "Arial Narrow", sans-serif;
    font-size: 24px;
    letter-spacing: 1px;
    text-transform: uppercase;
    color: var(--paper-text);
  }
</style>
</head>
<body>
  <section class="card card-front">
    <div class="name-band"></div>
    <h1 class="person-name">Liam Varga</h1>
    <p class="person-role">Director</p>
    <p class="brand-name">Summit Glossfloor<br>&amp; Honing</p>
    <ul class="contact-list">
      <li>
        <svg viewBox="0 0 24 24" aria-hidden="true"><path d="M6.6 10.8a15.1 15.1 0 0 0 6.6 6.6l2.2-2.2c.3-.3.7-.4 1-.2 1.1.4 2.3.6 3.6.6.6 0 1 .4 1 1V20c0 .6-.4 1-1 1A17 17 0 0 1 3 4c0-.6.4-1 1-1h3.5c.6 0 1 .4 1 1 0 1.3.2 2.5.6 3.6.1.3 0 .7-.2 1z"/></svg>
        <span>0491735082</span>
      </li>
      <li>
        <svg viewBox="0 0 24 24" aria-hidden="true"><path d="M2 5h20v14H2zm2 2v.4l8 5.2 8-5.2V7zm0 2.8V17h16V9.8l-8 5.2z"/></svg>
        <span>info@summitgfh.com.au</span>
      </li>
    </ul>
    <p class="website">www.summitglossfloor.com.au</p>
  </section>

  <section class="card card-back">
    <p class="brand-name">Summit Glossfloor<br>&amp; Honing</p>
    <p class="sectors">Commercial - Domestic - Industrial</p>
  </section>
</body>
</html>
```